IT’S NOT A CLEANING, IT’S YOUR LIFE! TOP TEN REASONS WHY THIS IS NOT JUST A “CLEANING”

We made a list for our patients to let them know why our hygiene appointments are different than other cleanings. Since this is a lot of information, we would like it easily readable within 4-5 feet but we do not want the post to be HUGE. Please see below:

IT’S NOT A CLEANING, IT’S YOUR LIFE!
TOP TEN REASONS WHY THIS IS NOT JUST A “CLEANING”

10. We make you look better. Healthy teeth and gums are more attractive. Recent studies
show that the smile is the first thing people notice and that people with better looking teeth
are more confident and successful.

9. We can relieve your headaches. During your hygiene visit we evaluate for serious bite
issues, many of which lead to muscle soreness, headaches, and migraines.

8. We check for oral cancer. Oral cancer kills 1 person per hour 24 hours a day. The death rate for oral cancer is higher than cancers we routinely hear about such as cervical, thyroid and skin cancer.

7. We make you smell better. During your hygiene visit we eliminate many of the germs that live under your gum tissue and cause bad breath.

6. We save you money. By utilizing the latest dental technology (digital x-rays, mouth
cameras, and magnification glasses) we can help with early detection of tooth and gum
problems and save you the cost of gum surgery, root canals, and implants.

5. We clean in places you cannot. We clean under the gum line and between teeth where
most of the germs hide and cause dental disease. 40% of the bacteria in your mouth lives in
between your teeth.

4. We prevent pain. We identify tooth decay that can lead to nerve involvement and pain,
root canal, and tooth loss.

3. We save your teeth. Most tooth loss is from periodontal/gum disease. At each visit we
evaluate the health of your gums and bone with our periodontal screening. Periodontal
disease, like high blood pressure, is symptomless until it is in advanced stages.

2. We protect your loved ones. Studies have proven that the bacteria that cause dental
disease can be transmitted from person to person. Think about that the next time you kiss
someone!

1. We prolong life. Researchers have linked the inflammation and infection found in the
mouth to heart attacks, strokes, and Alzheimer’s. By reducing infection in your mouth we can
greatly improve your overall health!

```html
<!DOCTYPE html>
<html lang="en">
<head>
<meta charset="utf-8">
<title>It's Not a Cleaning, It's Your Life</title>
<link href="https://fonts.googleapis.com/css2?family=Oswald:wght@700&family=Roboto+Condensed:wght@400&display=swap" rel="stylesheet">
<style>
  :root {
    --page-bg: #e9e9e9;
    --poster-white: #ffffff;
    --coat-shade: #dfe3e7;
    --coat-light: #f3f5f7;
    --accent-blue: #12a4e3;
    --body-grey: #5f6165;
  }
  * { margin: 0; padding: 0; box-sizing: border-box; }
  html, body {
    width: 890px;
    height: 1200px;
    overflow: hidden;
    background: var(--page-bg);
  }
  .poster {
    position: absolute;
    left: 78px;
    top: 33px;
    width: 734px;
    height: 1134px;
    background: var(--poster-white);
    box-shadow: 0 2px 10px rgba(0,0,0,0.18);
    overflow: hidden;
  }
  .poster-photo {
    position: absolute;
    inset: 0 0 120px 0;
    background:
      linear-gradient(180deg, rgba(255,255,255,0) 55%, var(--poster-white) 100%),
      radial-gradient(ellipse at 40% 20%, var(--coat-light) 0%, var(--coat-shade) 70%, #d2d7dc 100%);
  }
  .headline {
    position: absolute;
    left: 77px;
    top: 386px;
    font-family: "Oswald", sans-serif;
    font-weight: 700;
    font-size: 50px;
    line-height: 44px;
    color: var(--accent-blue);
    text-transform: uppercase;
    letter-spacing: -0.5px;
  }
  .reasons {
    position: absolute;
    left: 77px;
    top: 604px;
    width: 580px;
    list-style: none;
    font-family: "Roboto Condensed", sans-serif;
    font-size: 12px;
    line-height: 16px;
    color: var(--body-grey);
  }
  .reason {
    display: flex;
    gap: 11px;
    margin-bottom: 17px;
  }
  .reason-number {
    flex: 0 0 15px;
    height: 15px;
    border-radius: 50%;
    background: var(--accent-blue);
    color: var(--poster-white);
    font-size: 9px;
    line-height: 15px;
    text-align: center;
    font-weight: 400;
    margin-top: 1px;
  }
</style>
</head>
<body>
  <main class="poster">
    <div class="poster-photo" role="img" aria-label="Dental mirrors and probes tucked in the breast pocket of a white dentist's coat"></div>

    <h1 class="headline">It’s not a cleaning,<br>it’s your life!<br>Top ten reasons why this is<br>not just a “cleaning”</h1>

    <ol class="reasons">
      <li class="reason"><span class="reason-number">10</span><p>We make you look better. Healthy teeth and gums are more attractive. Recent studies show that the smile is the first thing people notice and that people with better looking teeth are more confident and successful.</p></li>
      <li class="reason"><span class="reason-number">9</span><p>We can relieve your headaches. During your hygiene visit we evaluate for serious bite issues, many of which lead to muscle soreness, headaches, and migraines.</p></li>
      <li class="reason"><span class="reason-number">8</span><p>We check for oral cancer. Oral cancer kills 1 person per hour 24 hours a day. The death rate for oral cancer is higher than cancers we routinely hear about such as cervical, thyroid and skin cancer.</p></li>
      <li class="reason"><span class="reason-number">7</span><p>We make you smell better. During your hygiene visit we eliminate many of the germs that live under your gum tissue and cause bad breath.</p></li>
      <li class="reason"><span class="reason-number">6</span><p>We save you money. By utilizing the latest dental technology (digital x-rays, mouth cameras, and magnification glasses) we can help with early detection of tooth and gum problems and save you the cost of gum surgery, root canals, and implants.</p></li>
      <li class="reason"><span class="reason-number">5</span><p>We clean in places you cannot. We clean under the gum line and between teeth where most of the germs hide and cause dental disease. 40% of the bacteria in your mouth lives in between your teeth.</p></li>
      <li class="reason"><span class="reason-number">4</span><p>We prevent pain. We identify tooth decay that can lead to nerve involvement and pain, root canal, and tooth loss.</p></li>
      <li class="reason"><span class="reason-number">3</span><p>We save your teeth. Most tooth loss is from periodontal/gum disease. At each visit we evaluate the health of your gums and bone with our periodontal screening. Periodontal disease, like high blood pressure, is symptomless until it is in advanced stages.</p></li>
      <li class="reason"><span class="reason-number">2</span><p>We protect your loved ones. Studies have proven that the bacteria that cause dental disease can be transmitted from person to person. Think about that the next time you kiss someone!</p></li>
      <li class="reason"><span class="reason-number">1</span><p>We prolong life. Researchers have linked the inflammation and infection found in the mouth to heart attacks, strokes, and Alzheimer’s. By reducing infection in your mouth we can greatly improve your overall health!</p></li>
    </ol>
  </main>
</body>
</html>
```